Spirits Bottle Label for American Agave Spirit produced in Maryland

Need to revamp my spirits bottle label to a new innovative design. Looking for a minimalist design that would catch your eye on in a liquor store bottle. I open to designs. Looking for something a lot different than what I currently have wow me with your creativity.

Design Brief:

Logo Name: "Tides" with the "H" positioned horizontally (emphasize the unique horizontal "H").
Color Scheme: Pink or Burgundy and gold (use these as primary colors). With gold being a accent color.
Motto: Include the phrase "Celebrate life with old and new friends" in a subtle, elegant font. Want to keep the 1947 but not as prominent as it is now.
Overall Feel: The design should convey warmth, celebration, and connection, blending a modern touch with timeless appeal.

I also attached a copy of my other brand bottle design thatI love. Barrel & Reed is the name

Target Market(s)

21-65 Year old spirits drinkers, A label that is different than most spirits bottles. Want to catch the eyes of consumers

Industry/Entity Type

spirits industy

Colors

Designer to choose colors to be used in the design.

Requirements
Must have
• Motto, vibrant colors, minimist design
Should not have
• Need to look professional and not be so cluttered

```html
<!DOCTYPE html>
<html lang="en">
<head>
<meta charset="utf-8">
<title>Tides American Agave Spirit Label</title>
<link href="https://fonts.googleapis.com/css2?family=Playfair+Display:wght@400;700&family=Montserrat:wght@400;600;700&family=Great+Vibes&display=swap" rel="stylesheet">
<style>
  :root {
    --page-bg: #f4f4f4;
    --gold-light: #f3e3a0;
    --gold: #c9a23a;
    --gold-deep: #8f6a1c;
    --burgundy: #4a0b2c;
    --berry: #8e1450;
    --pink: #d2377c;
    --blush: #f0b8d2;
    --white: #ffffff;
  }
  html, body {
    margin: 0;
    padding: 0;
    width: 1200px;
    height: 1199px;
    overflow: hidden;
    background: var(--page-bg);
  }
  .label {
    position: absolute;
    left: 186px;
    top: 50px;
    width: 828px;
    height: 1100px;
    box-sizing: border-box;
    padding: 34px 36px;
    background: linear-gradient(135deg, var(--gold-deep) 0%, var(--gold) 25%, var(--gold-light) 50%, var(--gold) 72%, var(--gold-deep) 100%);
  }
  .label-panel {
    position: relative;
    width: 756px;
    height: 1032px;
    border-radius: 16px;
    overflow: hidden;
  }
  .agave-art {
    position: absolute;
    inset: 0;
    background:
      radial-gradient(ellipse 55% 45% at 52% 70%, var(--pink) 0%, rgba(210,55,124,0) 70%),
      radial-gradient(ellipse 40% 35% at 45% 20%, var(--blush) 0%, rgba(240,184,210,0) 75%),
      linear-gradient(160deg, var(--berry) 0%, var(--burgundy) 45%, var(--berry) 75%, var(--burgundy) 100%);
  }
  .panel-text {
    position: absolute;
    color: var(--white);
    font-family: "Montserrat", sans-serif;
    margin: 0;
  }
  .small-batch {
    left: 87px;
    top: 124px;
    font-size: 19px;
    font-weight: 600;
    letter-spacing: 0.5px;
  }
  .abv {
    right: 59px;
    top: 122px;
    font-size: 21px;
    font-weight: 600;
  }
  .motto {
    left: 0;
    right: 0;
    top: 344px;
    text-align: center;
    font-size: 14px;
    font-weight: 700;
    line-height: 19px;
    letter-spacing: 0.3px;
  }
  .brand-name {
    left: 0;
    right: 0;
    top: 452px;
    text-align: center;
    font-family: "Playfair Display", serif;
    font-weight: 700;
    font-size: 110px;
    line-height: 1;
    letter-spacing: 28px;
    padding-left: 28px;
    color: var(--gold);
  }
  .category {
    left: 0;
    right: 0;
    top: 590px;
    text-align: center;
    font-size: 37px;
    font-weight: 400;
    line-height: 52px;
    letter-spacing: 1px;
  }
  .spirit-word {
    left: 0;
    right: 0;
    top: 700px;
    text-align: center;
    font-family: "Great Vibes", cursive;
    font-size: 60px;
    line-height: 1;
  }
  .spirit-swash {
    position: absolute;
    left: 250px;
    top: 690px;
  }
  .volume {
    left: 129px;
    top: 898px;
    font-size: 28px;
    font-weight: 700;
  }
  .heritage {
    left: 547px;
    top: 882px;
    width: 100px;
    text-align: center;
    line-height: 1;
  }
  .heritage-since {
    display: block;
    font-family: "Playfair Display", serif;
    font-size: 9px;
    letter-spacing: 0.5px;
  }
  .heritage-year {
    display: block;
    font-family: "Playfair Display", serif;
    font-size: 30px;
    margin-top: 4px;
  }
</style>
</head>
<body>
  <main class="label">
    <div class="label-panel">
      <div class="agave-art" role="img" aria-label="Illustration of layered pink and burgundy agave leaves radiating from the centre"></div>

      <p class="panel-text small-batch">SMALL BATCH</p>
      <p class="panel-text abv">ALC.40% BY VOL.</p>

      <p class="panel-text motto">CELEBRATE LIFE WITH OLD<br>AND NEW FRIENDS</p>

      <h1 class="panel-text brand-name">TIDES</h1>
      <p class="panel-text category">AMERICAN<br>AGAVE</p>

      <svg class="spirit-swash" width="300" height="90" viewBox="0 0 300 90" aria-hidden="true">
        <path d="M20 80 C 110 55, 200 30, 290 6" fill="none" stroke="#ffffff" stroke-width="2"/>
      </svg>
      <p class="panel-text spirit-word">Spirit</p>

      <p class="panel-text volume">750 ml</p>
      <p class="panel-text heritage">
        <span class="heritage-since">SINCE</span>
        <span class="heritage-year">1947</span>
      </p>
    </div>
  </main>
</body>
</html>
```